Napa Winery - Chardonnay wine label

We are looking for a label for a new Napa Valley winery - chardonnay wine. The winery is "Marrowbrook Hill Vintners" and we would like to see it depicted on a white wine (chardonnay style) bottle. The winery is called Marrowbrook Hill Vintners.

We are open to ideas!

Target Market(s)

High-end chardonnay lovers

Requirements
Nice to have
• Painted or etched label onto bottle

```html
<!DOCTYPE html>
<html lang="en">
<head>
<meta charset="utf-8">
<title>Marrowbrook Hill Vintners – Chardonnay Label</title>
<link rel="stylesheet" href="https://fonts.googleapis.com/css2?family=Pinyon+Script&family=Mrs+Saint+Delafield&family=Cormorant+Garamond:wght@500&display=swap">
<style>
  :root {
    --backdrop: #f4f3ef;
    --paper: #ecebea;
    --copper: #b98a6e;
    --copper-deep: #9c6f56;
    --ink: #5d5a57;
    --silver: #b4b2b0;
    --silver-light: #d2d0ce;
    --faint: #b9b7b5;
  }
  * { box-sizing: border-box; margin: 0; padding: 0; }
  html, body {
    width: 1200px; height: 1000px; overflow: hidden;
    background: var(--backdrop);
  }
  .canvas {
    position: relative; width: 1200px; height: 1000px;
  }
  .label {
    position: absolute; left: 280px; top: 100px;
    width: 640px; height: 800px;
    background: var(--paper);
    box-shadow: 0 2px 10px rgba(0,0,0,0.08);
    text-align: center;
  }
  .winery-name {
    position: absolute; top: 90px; left: 0; right: 0;
    font-family: "Pinyon Script", cursive;
    font-size: 56px; font-weight: 400;
    color: var(--copper);
    white-space: nowrap;
  }
  .wreath {
    position: absolute; left: 150px; top: 220px;
    width: 340px; height: 340px;
  }
  .varietal {
    position: absolute; top: 365px; left: 0; right: 0;
    font-family: "Cormorant Garamond", serif;
    font-weight: 500; font-size: 30px; letter-spacing: 1px;
    color: var(--copper-deep);
  }
  .region {
    position: absolute; top: 398px; left: 0; right: 0;
    font-family: "Mrs Saint Delafield", cursive;
    font-size: 30px; color: var(--faint);
  }
  .details {
    position: absolute; top: 640px; left: 0; right: 0;
    display: flex; flex-direction: column; align-items: center;
    color: var(--ink);
  }
  .origin {
    font-family: "Cormorant Garamond", serif;
    font-size: 17px; letter-spacing: 0.5px;
  }
  .rule {
    width: 90px; height: 1px; background: var(--copper);
    margin: 5px 0;
  }
  .volume, .note {
    font-family: Arial, Helvetica, sans-serif;
    font-size: 12px;
  }
  .note { margin-top: 4px; }
</style>
</head>
<body>
<div class="canvas">
  <section class="label">
    <h1 class="winery-name">Marrowbrook Hill Vintners</h1>

    <svg class="wreath" viewBox="0 0 340 340" role="img" aria-label="Circular ornamental wreath of grape clusters and vine leaves">
      <defs>
        <radialGradient id="wreathTone" cx="50%" cy="50%" r="50%">
          <stop offset="70%" stop-color="var(--silver)"/>
          <stop offset="100%" stop-color="var(--silver-light)"/>
        </radialGradient>
      </defs>
      <path fill="url(#wreathTone)" fill-rule="evenodd"
        d="M170 0 A170 170 0 1 1 169.9 0 Z M170 45 A125 125 0 1 0 170.1 45 Z"/>
    </svg>

    <p class="varietal">CHARDONNAY</p>
    <p class="region">Napa Valley</p>

    <div class="details">
      <p class="origin">PRODUCT OF LOREM 2010</p>
      <span class="rule"></span>
      <p class="volume">120% vol 750 ml</p>
      <span class="rule"></span>
      <p class="note">Lorem ipsum dolor sit amet, consectetur</p>
    </div>
  </section>
</div>
</body>
</html>
```